Kaede Roasters

Full Shopify site .
About page

Merch page
Tshirts, hats, mugs

Coffee page
-sections
Single origin
Tomoe series
Sensu series
Decaf

KaedeX page
Cold brew
Coffee liquor
Absinthe Coffee

```html
<!DOCTYPE html>
<html lang="en">
<head>
<meta charset="utf-8">
<title>Kaede Roasters</title>
<link href="https://fonts.googleapis.com/css2?family=Poppins:wght@400;500;600;700&family=Jost:wght@400;500;600&display=swap" rel="stylesheet">
<style>
:root{
  --red:#e3262f;
  --red-dark:#b81b24;
  --ink:#1b1b1b;
  --text:#333;
  --blush:#f3e3ef;
  --sand:#ead9ad;
  --rose:#f6e1e5;
  --white:#fff;
  --black:#000;
}
*{box-sizing:border-box;margin:0;padding:0}
html,body{width:1200px;height:4471px;overflow:hidden}
body{position:relative;font-family:"Jost",sans-serif;color:var(--text);background:var(--white)}
.abs{position:absolute}
.head{font-family:"Poppins",sans-serif;color:var(--ink);font-weight:700;text-transform:uppercase}
.head b{font-weight:700}
.head span{font-weight:500}
.btn{position:absolute;background:var(--red);color:#fff;font-family:"Poppins",sans-serif;font-weight:600;font-size:14px;border-radius:22px;display:flex;align-items:center;justify-content:center;text-transform:uppercase}
.ph{position:absolute}
/* header */
.site-header{position:absolute;left:0;top:0;width:1200px;height:85px;background:#fff;z-index:5}
.nav a{position:absolute;top:33px;font-family:"Poppins",sans-serif;font-size:15px;font-weight:500;color:var(--ink);text-decoration:none}
.nav a.active{color:var(--red);font-weight:600}
.brand{position:absolute;left:528px;top:0;width:144px;height:144px;border-radius:50%;background:#fff;z-index:6;display:flex;flex-direction:column;align-items:center;justify-content:center}
.brand i{display:block;width:58px;height:58px;border-radius:50%;background:var(--red);margin-bottom:6px}
.brand b{font-family:"Poppins",sans-serif;font-size:20px;font-weight:700;color:var(--ink)}
.cart-count{position:absolute;left:940px;top:26px;width:14px;height:14px;border-radius:50%;background:var(--red);color:#fff;font-size:9px;display:flex;align-items:center;justify-content:center}
/* hero */
.hero-art{left:0;top:85px;width:1200px;height:630px;background:linear-gradient(180deg,#b8477a 0%,#c95a86 40%,#8d4f86 70%,#3f3a6f 100%)}
.hero-copy{left:112px;top:215px;color:#fff}
.hero-copy h1{font-family:"Poppins",sans-serif;font-size:44px;font-weight:700;text-transform:uppercase;line-height:1.1}
.hero-copy h2{font-family:"Poppins",sans-serif;font-size:25px;font-weight:600;line-height:1.4;margin-top:12px}
.hero-copy p{font-size:15px;line-height:1.55;margin-top:14px;width:430px}
/* about */
.about{left:0;top:712px;width:1200px;height:643px;background:var(--blush)}
.copy p{font-size:16px;line-height:1.75;color:var(--text);margin-bottom:22px}
.rule{display:inline-block;width:62px;height:3px;background:var(--red);vertical-align:middle;margin:0 8px}
/* coffee */
.coffee{left:0;top:1355px;width:1200px;height:570px;background:var(--sand)}
.card{position:absolute;background:#fff;border-radius:6px;overflow:hidden;text-align:center;box-shadow:0 2px 8px rgba(0,0,0,.08)}
.card h3{font-family:"Poppins",sans-serif;font-size:17px;font-weight:600;color:var(--ink);text-transform:uppercase;margin-top:24px}
.card p{font-size:16px;line-height:1.45;color:var(--text);margin:6px 18px 0}
.card .go{position:absolute;left:50%;bottom:22px;margin-left:-9px;width:18px;height:18px}
/* featured */
.featured{left:0;top:2700px;width:1200px;height:620px;background:var(--rose)}
.prod h3{font-family:"Poppins",sans-serif;font-size:18px;font-weight:600;color:var(--ink);text-transform:uppercase;margin-top:20px}
.prod .price{font-family:"Poppins",sans-serif;color:var(--red);font-weight:600;font-size:19px;margin-top:4px}
.circle-arrow{position:absolute;width:34px;height:34px}
/* testimonials */
.t-card{position:absolute;width:233px;height:220px;background:#f2f2f2;border-radius:8px;padding:26px 30px}
.stars{color:#f0b326;font-size:13px;letter-spacing:2px}
.t-card p{font-size:10.5px;line-height:1.5;color:#333;margin-top:8px}
.who{display:flex;align-items:center;margin-top:10px}
.who i{width:40px;height:40px;border-radius:50%;background:#c9a07e;margin-right:14px}
.who b{display:block;font-family:"Poppins",sans-serif;font-size:12px;font-weight:600;color:var(--ink)}
.who small{font-size:9px;color:#666}
/* footer */
.footer{left:0;top:4050px;width:1200px;height:421px;background:var(--black);color:#fff}
.footer h4{font-family:"Poppins",sans-serif;font-size:19px;font-weight:600;position:absolute}
.f-row{position:absolute;display:flex;align-items:center;font-size:14px}
.f-row i{width:36px;height:36px;border-radius:50%;background:var(--red);margin-right:14px;display:flex;align-items:center;justify-content:center}
.social{position:absolute;width:29px;height:29px;background:#fff;border-radius:5px}
.social::after{content:"";position:absolute;left:9px;top:9px;width:11px;height:11px;border-radius:2px;background:var(--red)}
</style>
</head>
<body>

<header class="site-header">
  <nav class="nav">
    <a class="active" style="left:112px">HOME</a>
    <a style="left:216px">ABOUT US</a>
    <a style="left:354px">KAEDEX</a>
    <a style="left:741px">COFFEE</a>
    <a style="left:836px">MERCH</a>
  </nav>
  <svg class="abs" style="left:914px;top:30px" width="28" height="28" viewBox="0 0 24 24" aria-hidden="true"><path d="M1 3h3l3 11h11l3-8H6" fill="none" stroke="#111" stroke-width="2"/><path d="M7 8h13l-2 5H8z" fill="#111"/><circle cx="9" cy="19" r="2" fill="#111"/><circle cx="17" cy="19" r="2" fill="#111"/></svg>
  <span class="cart-count">0</span>
  <span class="btn" style="left:970px;top:22px;width:120px;height:40px;font-size:15px">Shop Now</span>
</header>
<div class="brand"><i></i><b>KAEDE</b></div>

<!-- hero -->
<div class="ph hero-art" role="img" aria-label="Illustration of a figure holding a cup before a red sun, mountains and a blossoming tree at dusk"></div>
<svg class="abs" style="left:0;top:560px" width="1200" height="160" viewBox="0 0 1200 160" aria-hidden="true">
  <path d="M0 20 C300 140 800 150 1200 40 L1200 160 L0 160Z" fill="#f3e3ef"/>
  <path d="M0 20 C300 140 800 150 1200 40" fill="none" stroke="#e3262f" stroke-width="14"/>
  <path d="M0 36 C320 150 820 160 1200 56" fill="none" stroke="#fff" stroke-width="5"/>
  <path d="M0 46 C320 160 820 170 1200 66" fill="none" stroke="#b81b24" stroke-width="4"/>
</svg>
<div class="abs hero-copy">
  <h1>Kaede Roasters</h1>
  <h2>Precision Roasted Coffee.<br>Inspired by Balance.</h2>
  <p>Crafted in small batches. Rooted in discipline. Designed for those who appreciate clarity in every cup.</p>
</div>
<span class="btn" style="left:110px;top:422px;width:118px;height:40px">Shop Now</span>

<!-- about -->
<section class="abs about"></section>
<div class="ph" role="img" aria-label="Coffee cherries, cup and roasted beans" style="left:123px;top:823px;width:262px;height:219px;background:linear-gradient(135deg,#5e7a33,#8c3b22,#e2b46b)"></div>
<div class="ph" role="img" aria-label="Takeaway paper coffee cup" style="left:400px;top:900px;width:181px;height:298px;background:linear-gradient(180deg,#2a2620,#a3794b 60%,#3a332b)"></div>
<div class="ph" role="img" aria-label="Steaming cup of coffee on a table" style="left:182px;top:1060px;width:202px;height:181px;background:linear-gradient(135deg,#d9d3c8,#8d8274)"></div>
<div class="abs" style="left:337px;top:1004px;width:96px;height:96px;border-radius:50%;background:#fff;display:flex;align-items:center;justify-content:center"><i style="width:70px;height:70px;border-radius:50%;background:var(--red);display:block"></i></div>
<div class="ph" role="img" aria-label="Coffee branch with red cherries" style="left:945px;top:690px;width:230px;height:180px;background:radial-gradient(circle at 50% 50%,#4f7a34,rgba(243,227,239,0) 70%)"></div>
<div class="abs copy" style="left:630px;top:852px;width:430px">
  <h2 class="head" style="font-size:31px;margin-bottom:18px"><b>Kaede</b> <span>Roasters</span><span class="rule"></span></h2>
  <p>At Kaede Roasters, coffee is more than a product—it is a practice.</p>
  <p>Inspired by the fleeting beauty of the sakura blossom, we pursue balance in every roast.</p>
  <p>Precision guides us. Simplicity defines us.<br>Every cup is intentional.</p>
</div>
<span class="btn" style="left:630px;top:1162px;width:134px;height:40px">Read More</span>

<!-- our coffee -->
<section class="abs coffee"></section>
<h2 class="abs head" style="left:0;top:1440px;width:1200px;text-align:center;font-size:32px"><span class="rule"></span><span>Our</span> <b>Coffee</b><span class="rule"></span></h2>
<div class="card" style="left:112px;top:1518px;width:223px;height:364px"><div role="img" aria-label="Espresso machine pouring into a cup" style="height:183px;background:linear-gradient(135deg,#2b2b2b,#8a8a8a)"></div><h3>Single Origin</h3><p>Pure expression of origin. Clean, nuanced, and honest.</p><svg class="go" viewBox="0 0 18 18"><circle cx="9" cy="9" r="9" fill="#e3262f"/><path d="M6 9h6M9 6l3 3-3 3" stroke="#fff" stroke-width="2" fill="none"/></svg></div>
<div class="card" style="left:363px;top:1518px;width:223px;height:364px"><div role="img" aria-label="Basket of red coffee cherries" style="height:183px;background:linear-gradient(135deg,#5c2a1c,#b11d2a)"></div><h3>Tomoe Series</h3><p>Our most refined coffees—rare, floral, and exceptional.</p><svg class="go" viewBox="0 0 18 18"><circle cx="9" cy="9" r="9" fill="#e3262f"/><path d="M6 9h6M9 6l3 3-3 3" stroke="#fff" stroke-width="2" fill="none"/></svg></div>
<div class="card" style="left:614px;top:1518px;width:223px;height:364px"><div role="img" aria-label="Espresso pouring into a glass" style="height:183px;background:linear-gradient(135deg,#6d8ea3,#9b5a22)"></div><h3>Sensu Series</h3><p>Bold profiles with depth and intensity. Coffee without compromise.</p><svg class="go" viewBox="0 0 18 18"><circle cx="9" cy="9" r="9" fill="#e3262f"/><path d="M6 9h6M9 6l3 3-3 3" stroke="#fff" stroke-width="2" fill="none"/></svg></div>
<div class="card" style="left:865px;top:1518px;width:223px;height:364px"><div role="img" aria-label="Latte with foam art" style="height:183px;background:linear-gradient(135deg,#3d3935,#c2a27e)"></div><h3>Decaf</h3><p>All the flavor. None of the noise.</p><svg class="go" viewBox="0 0 18 18"><circle cx="9" cy="9" r="9" fill="#e3262f"/><path d="M6 9h6M9 6l3 3-3 3" stroke="#fff" stroke-width="2" fill="none"/></svg></div>
<div class="ph" role="img" aria-label="Band of roasted coffee beans" style="left:0;top:1915px;width:1200px;height:143px;background:linear-gradient(180deg,rgba(234,217,173,0),#7a3d1f 35%,#4a2411)"></div>

<!-- art of balance -->
<div class="ph" role="img" aria-label="Faint blossom tree and mountain backdrop" style="left:0;top:2058px;width:1200px;height:642px;background:linear-gradient(180deg,#fff 0%,#fbf3f5 70%,#f2e7ea 100%)"></div>
<div class="ph" role="img" aria-label="Bonsai tree in a pot with red sun" style="left:0;top:2110px;width:90px;height:170px;background:radial-gradient(circle at 40% 40%,#f0a3b6,rgba(255,255,255,0) 70%)"></div>
<div class="abs copy" style="left:112px;top:2212px;width:470px">
  <h2 class="head" style="font-size:31px;margin-bottom:14px"><b>The Art</b> <span>of Balance</span><span class="rule"></span></h2>
  <p>At <strong>Kaede Roasters</strong>, coffee is more than a product—it is a practice.</p>
  <p>Inspired by the fleeting beauty of the sakura blossom, we pursue balance in every roast.</p>
  <p>Precision guides us. Simplicity defines us.<br>Every cup is intentional.</p>
</div>
<span class="btn" style="left:112px;top:2522px;width:134px;height:40px">Read More</span>
<svg class="abs" style="left:670px;top:2250px" width="340" height="300" aria-hidden="true"><path d="M2 150V3h60M338 230v68H200" fill="none" stroke="#e3262f" stroke-width="5"/></svg>
<div class="ph" role="img" aria-label="Coffee bag and steaming cup on a dark table" style="left:722px;top:2180px;width:368px;height:325px;background:linear-gradient(135deg,#16232c,#2c3e4a 60%,#5a4330)"></div>
<div class="ph" role="img" aria-label="Pour-over coffee brewer in a café" style="left:630px;top:2403px;width:263px;height:203px;background:linear-gradient(135deg,#1f2a22,#8b5a2b);border-top:6px solid #fff;border-right:6px solid #fff"></div>

<!-- featured -->
<section class="abs featured"></section>
<h2 class="abs head" style="left:0;top:2785px;width:1200px;text-align:center;font-size:32px"><span class="rule" style="width:55px"></span><b>Featured</b> <span>Coffees</span><span class="rule" style="width:55px"></span></h2>
<p class="abs" style="left:0;top:2830px;width:1200px;text-align:center;font-size:17px;color:#222">Selected for clarity, balance, and character.</p>
<div class="card prod" style="left:112px;top:2885px;width:226px;height:322px;border-radius:4px"><div role="img" aria-label="Burlap sack of coffee beans" style="margin:10px;height:212px;background:#ececec;border-radius:4px"></div><h3>Single Origin</h3><div class="price">$54.00</div></div>
<div class="card prod" style="left:361px;top:2885px;width:226px;height:322px;border-radius:4px"><div role="img" aria-label="Kraft coffee bag" style="margin:10px;height:212px;background:#ececec;border-radius:4px"></div><h3>Tomoe Series</h3><div class="price">$54.00</div></div>
<div class="card prod" style="left:610px;top:2885px;width:226px;height:322px;border-radius:4px"><div role="img" aria-label="White and brown coffee pouches" style="margin:10px;height:212px;background:#ececec;border-radius:4px"></div><h3>Sensu Series</h3><div class="price">$54.00</div></div>
<div class="card prod" style="left:860px;top:2885px;width:226px;height:322px;border-radius:4px"><div role="img" aria-label="Paper coffee bag with spilled beans" style="margin:10px;height:212px;background:#ececec;border-radius:4px"></div><h3>Decaf</h3><div class="price">$54.00</div></div>
<svg class="circle-arrow" style="left:40px;top:3008px" viewBox="0 0 34 34" aria-hidden="true"><circle cx="17" cy="17" r="15" fill="none" stroke="#333" stroke-width="1.5"/><path d="M19 11l-6 6 6 6" fill="none" stroke="#333" stroke-width="1.5"/></svg>
<svg class="circle-arrow" style="left:1123px;top:3008px" viewBox="0 0 34 34" aria-hidden="true"><circle cx="17" cy="17" r="15" fill="none" stroke="#333" stroke-width="1.5"/><path d="M15 11l6 6-6 6" fill="none" stroke="#333" stroke-width="1.5"/></svg>
<div class="ph" role="img" aria-label="Bonsai with red sun" style="left:1110px;top:3080px;width:90px;height:170px;background:radial-gradient(circle at 50% 40%,#f0a3b6,rgba(246,225,229,0) 70%)"></div>
<svg class="abs" style="left:0;top:3255px" width="1200" height="170" viewBox="0 0 1200 170" aria-hidden="true">
  <path d="M0 10 C300 150 850 160 1200 40 L1200 170 L0 170Z" fill="#fff"/>
  <path d="M0 10 C300 150 850 160 1200 40" fill="none" stroke="#e3262f" stroke-width="14"/>
  <path d="M0 26 C320 160 860 170 1200 58" fill="none" stroke="#fff" stroke-width="5"/>
  <path d="M0 36 C320 170 860 180 1200 68" fill="none" stroke="#b81b24" stroke-width="4"/>
</svg>

<!-- testimonials -->
<div class="ph" role="img" aria-label="Faint misty blossom trees" style="left:0;top:3413px;width:1200px;height:500px;background:linear-gradient(180deg,#fff,#f6eef0 50%,#fff)"></div>
<h2 class="abs head" style="left:0;top:3500px;width:1200px;text-align:center;font-size:32px"><span class="rule" style="width:55px"></span><span>Client</span> <b>Testimonials</b><span class="rule" style="width:55px"></span></h2>
<div class="t-card" style="left:112px;top:3575px"><div class="stars">★★★★★</div><p>Lorem ipsum dolor sit amet, consectetur adipiscing elit, sed do eiusmod tempor incididunt ut labore et dolore magna aliqua. Ut enim ad minim veniam, quis nostrud exercitation ullamco l</p><div class="who"><i></i><div><b>Daniel Hart</b><small>2 Days Ago</small></div></div></div>
<div class="t-card" style="left:363px;top:3575px"><div class="stars">★★★★★</div><p>Lorem ipsum dolor sit amet, consectetur adipiscing elit, sed do eiusmod tempor incididunt ut labore et dolore magna aliqua. Ut enim ad minim veniam, quis nostrud exercitation ullamco l</p><div class="who"><i></i><div><b>Daniel Hart</b><small>2 Days Ago</small></div></div></div>
<div class="t-card" style="left:607px;top:3575px"><div class="stars">★★★★★</div><p>Lorem ipsum dolor sit amet, consectetur adipiscing elit, sed do eiusmod tempor incididunt ut labore et dolore magna aliqua. Ut enim ad minim veniam, quis nostrud exercitation ullamco l</p><div class="who"><i></i><div><b>Daniel Hart</b><small>2 Days Ago</small></div></div></div>
<div class="t-card" style="left:852px;top:3575px"><div class="stars">★★★★★</div><p>Lorem ipsum dolor sit amet, consectetur adipiscing elit, sed do eiusmod tempor incididunt ut labore et dolore magna aliqua. Ut enim ad minim veniam, quis nostrud exercitation ullamco l</p><div class="who"><i></i><div><b>Daniel Hart</b><small>2 Days Ago</small></div></div></div>
<svg class="abs" style="left:40px;top:3670px" width="36" height="24" viewBox="0 0 36 24" aria-hidden="true"><path d="M34 12H4M13 3l-9 9 9 9" fill="none" stroke="#111" stroke-width="2.5"/></svg>
<svg class="abs" style="left:1120px;top:3670px" width="36" height="24" viewBox="0 0 36 24" aria-hidden="true"><path d="M2 12h30M23 3l9 9-9 9" fill="none" stroke="#111" stroke-width="2.5"/></svg>

<!-- footer -->
<svg class="abs" style="left:0;top:3900px" width="1200" height="160" viewBox="0 0 1200 160" aria-hidden="true">
  <path d="M0 150 C350 20 850 10 1200 110 L1200 160 L0 160Z" fill="#000"/>
  <path d="M0 140 C350 10 850 0 1200 100" fill="none" stroke="#e3262f" stroke-width="14"/>
  <path d="M0 124 C350 0 850 -8 1200 84" fill="none" stroke="#b81b24" stroke-width="4"/>
</svg>
<footer class="abs footer">
  <div class="abs" style="left:130px;top:40px;width:220px;text-align:center">
    <i style="display:block;margin:0 auto 14px;width:110px;height:110px;border-radius:50%;background:#fff"></i>
    <b style="font-family:'Poppins',sans-serif;font-size:30px;font-weight:700;letter-spacing:2px">KAEDE</b>
    <div style="font-size:15px;letter-spacing:3px">ROASTERS</div>
  </div>
  <span class="social" style="left:164px;top:268px"></span>
  <span class="social" style="left:203px;top:268px"></span>
  <span class="social" style="left:242px;top:268px"></span>
  <span class="social" style="left:280px;top:268px"></span>

  <h4 style="left:466px;top:32px">Contact Us</h4>
  <div class="f-row" style="left:466px;top:88px"><i><svg width="14" height="16" viewBox="0 0 14 16"><path d="M7 1a5 5 0 0 1 5 5c0 4-5 9-5 9S2 10 2 6a5 5 0 0 1 5-5z" fill="#fff"/><circle cx="7" cy="6" r="2" fill="#e3262f"/></svg></i>Company Name,United State.</div>
  <div class="f-row" style="left:466px;top:148px"><i><svg width="16" height="12" viewBox="0 0 16 12"><rect width="16" height="12" rx="1" fill="#fff"/><path d="M1 1l7 6 7-6" stroke="#e3262f" stroke-width="1.5" fill="none"/></svg></i>info@kaederoasters.com</div>
  <div class="f-row" style="left:466px;top:208px"><i><svg width="14" height="14" viewBox="0 0 14 14"><path d="M3 1l3 3-2 2c1 2 2 3 4 4l2-2 3 3-2 2C5 13 1 9 1 3z" fill="#fff"/></svg></i>+1888 8888 8888</div>

  <h4 style="left:807px;top:32px">Sign Up To Our Newsletter</h4>
  <p class="abs" style="left:807px;top:80px;width:300px;font-size:14px;line-height:1.9">Lorem ipsum dolor sit amet,consectetur adipiscing elit,adipiscing elit.</p>
  <div class="abs" style="left:810px;top:148px;width:270px;border-bottom:1px solid #fff;padding-bottom:8px;font-size:14px">Email</div>
  <span class="btn" style="left:815px;top:212px;width:145px;height:48px;font-size:16px;border-radius:26px;text-transform:none">Subscribe</span>

  <div class="abs" style="left:98px;top:347px;width:1003px;height:1px;background:#555"></div>
  <p class="abs" style="left:0;top:370px;width:1200px;text-align:center;font-size:15px;font-weight:500">Copyrights@2026.Company Name.All Rights Reserved</p>
</footer>

</body>
</html>
```